QBT Web Design Project

I would like a simple and elegant design for my international business consulting practice web site. I already have new QBT Logo and will have brochure-colors are blue, green and black

Practice areas:
I offer consulting services specializing in developing Internet-based anti-counterfeiting and anti-fraud programs, test purchases and investigations.

I offer Cyber Security, Data Protection and Compliance services

I also offer International Due Diligence Investigations and Country and Travel Risk Assessments

General Background Investigations

Physical Security Services

About me section listing my Bio

I have a set of key associates that I work with around the world and will want to list their CVs or Bios under "QBT

Associates"Banner with nice photo but not too cluttered

Ability to Upload documents and articles

Contact us section
Updates

I have uploaded my new logo-please advise if you didn't get it or it is not in the correct file format.

Thank you

Gordon

Hello Everyone,

Thank you for your submissions and ideas. I'm not sure about design only vs code. I understand that some of you do not do code-if not then please just provide design.

More about my business: see below link on Google docs to my brochure-this should help but don't use that phone number-see below.

https://files.example-docs.net/viewer?id=XK93PLQ7ZTR2MWN8&hl=en_US

 

Here are some details.

Contacts:

Gordon T. Vostrell, CPP

President

Vostrell and Partners, LLC

P.O. Box 47192

Gaithersburg, MD 20899

USA

web address:www.Vostrellandpartners.example (currently not working)

email:gord @vostrelland partners.example

Tel: 202-555-0147

I hope this is helpful. Gord

Reason: Sorry but during holiday period, have not had as much time to devote to this project. Thanks for your submissions.

Per my previous guidance, please keep designs simple and elegant and free from traditional security images with locks and chains-I prefer one or at most, two photos. Two colors- blue and green in addition to black for print. I want to present professional, corporate and international image. Thank you for your ideas nad submissions.

Gord

Target Market(s)

Law firms, large multi-national corporations, Security Industry

Industry/Entity Type

Business

Requirements
Must have
• Must have sections: (will provide text)

About QBT (will provide text)

Practice areas

Associates (will provide text)

Contact us

(it must also have ability to upload files and articles)
Should not have
• Old style fonts and symbols such as security badges, scales of justice, etc. I want a sleek and modern design.

```html
<!DOCTYPE html>
<html lang="en">
<head>
<meta charset="utf-8">
<title>QBT – Vostrell &amp; Partners, LLC</title>
<link rel="stylesheet" href="https://fonts.googleapis.com/css2?family=Francois+One&family=Open+Sans:wght@400&family=Arimo:wght@400;700&family=Archivo+Narrow:wght@400&family=Libre+Franklin:wght@300&family=Lato:wght@400&display=swap">
<style>
  :root {
    --navy: #05476e;
    --green: #6cd24a;
    --sky: #66c7fb;
    --sky-line: #78c9f2;
    --divider: #4aa6d8;
    --logo-blue: #1c5a96;
    --link-blue: #1aa0e0;
    --ink: #111;
    --grey: #555;
    --white: #fff;
  }
  * { box-sizing: border-box; margin: 0; padding: 0; }
  html, body { width: 1200px; height: 1188px; overflow: hidden; }
  body {
    position: relative;
    background: linear-gradient(to bottom, var(--navy) 0 574px, var(--white) 574px 744px, var(--green) 744px);
    font-family: "Arimo", Arial, sans-serif;
  }
  .page {
    position: absolute; left: 23px; top: 40px; width: 1154px; height: 1043px;
    background: var(--white);
    box-shadow: 0 0 6px rgba(0,0,0,.25);
  }
  .brand { position: absolute; left: 26px; top: 20px; }
  .brand-name {
    font-family: "Open Sans", sans-serif; font-size: 21px; color: var(--logo-blue);
    white-space: nowrap;
  }
  .brand-tagline {
    font-family: "Open Sans", sans-serif; font-size: 12.5px; color: var(--logo-blue);
    letter-spacing: 1.6px; margin-top: 2px; white-space: nowrap;
  }
  .main-nav {
    position: absolute; left: 591px; top: 45px; width: 566px; height: 29px;
    border-bottom: 3px solid var(--sky-line);
    display: flex; gap: 20px; padding-left: 16px;
    font-family: "Lato", sans-serif; font-size: 15px; color: var(--grey);
  }
  .main-nav a { color: inherit; text-decoration: none; position: relative; height: 26px; white-space: nowrap; }
  .main-nav a.is-current::after {
    content: ""; position: absolute; left: -16px; right: -10px; bottom: -3px; height: 3px;
    background: var(--green);
  }
  .hero {
    position: absolute; left: 23px; top: 91px; width: 1108px; height: 339px;
    background: linear-gradient(100deg, #06090e 0%, #0b1420 38%, #2d5a86 58%, #8fb4d8 72%, #2a4a6a 85%, #0a1622 100%);
    box-shadow: 2px 2px 5px rgba(0,0,0,.35);
  }
  .hero-title {
    position: absolute; left: 48px; top: 40px;
    font-family: "Francois One", sans-serif; font-weight: 400; font-size: 47px; line-height: 67px;
    color: var(--white); text-transform: uppercase; white-space: nowrap;
  }
  .hero-lede {
    position: absolute; left: 48px; top: 276px;
    font-size: 15px; color: var(--sky-line); white-space: nowrap;
  }
  .service-bar {
    position: absolute; left: 23px; top: 430px; width: 1108px; height: 77px;
    background: var(--sky); box-shadow: 2px 3px 5px rgba(0,0,0,.35);
    display: flex;
  }
  .service-item {
    display: flex; align-items: center; padding-left: 27px;
    font-size: 14px; font-weight: 700; color: var(--ink); text-decoration: none;
    text-transform: uppercase; border-left: 3px solid var(--divider); white-space: nowrap;
  }
  .service-item:first-child { border-left: none; padding-left: 47px; }
  .service-cyber { width: 212px; }
  .service-background { width: 376px; }
  .service-data { width: 199px; }
  .service-physical { flex: 1; }
  .intro {
    position: absolute; left: 68px; top: 556px; width: 1060px;
    font-family: "Libre Franklin", sans-serif; font-weight: 300;
    font-size: 24.5px; line-height: 34px; color: var(--green);
  }
  .intro-line { display: block; white-space: nowrap; }
  .cards { position: absolute; left: 22px; top: 701px; }
  .card {
    position: absolute; top: 0; width: 346px; height: 288px;
    border: 1px solid #e4eef4; background: var(--white);
  }
  .card-cyber { left: 0; }
  .card-physical { left: 387px; }
  .card-data { left: 762px; }
  .card-media { position: absolute; left: 4px; top: 3px; width: 338px; height: 209px; }
  .card-cyber .card-media { background: linear-gradient(135deg, #06122e, #1a4fa0 55%, #0a1a3a); }
  .card-physical .card-media { background: linear-gradient(90deg, #c9cdd1, #7d858c 40%, #2a2c30 55%, #b8bec4); }
  .card-data .card-media { background: linear-gradient(120deg, #0d0805, #3a2410 45%, #b07a2c 55%, #2a3f8a 80%, #0c0c14); }
  .card-title {
    position: absolute; left: 14px; top: 219px;
    font-family: "Archivo Narrow", "Arial Narrow", sans-serif; font-weight: 400;
    font-size: 19px; line-height: 24px; color: var(--link-blue); white-space: nowrap;
  }
  .card-text {
    position: absolute; left: 14px; top: 244px; width: 326px;
    font-family: "Archivo Narrow", "Arial Narrow", sans-serif;
    font-size: 12.5px; line-height: 17px; color: var(--grey);
  }
  .card-text span { display: block; white-space: nowrap; }
  .site-footer {
    position: absolute; right: 32px; top: 1101px;
    font-size: 13px; color: var(--white); white-space: nowrap;
  }
</style>
</head>
<body>
  <div class="page">
    <header>
      <div class="brand">
        <div class="brand-name">QBT | Vostrell &amp; Partners, LLC</div>
        <div class="brand-tagline">Intellectual Property and Cyber Security</div>
      </div>
      <nav class="main-nav">
        <a href="#" class="is-current">HOME</a>
        <a href="#">ABOUT QBT</a>
        <a href="#">PRACTICE AREAS</a>
        <a href="#">ASSOCIATES</a>
        <a href="#">CONTACT US</a>
      </nav>
    </header>

    <section class="hero" role="img" aria-label="Photo of a man at a window peering through venetian blinds">
      <h1 class="hero-title">Safe is not a<br>privilege.<br>It is a right.</h1>
      <p class="hero-lede">Lorem ipsum dolor sit amet, consectetur adipiscing elit.</p>
    </section>

    <nav class="service-bar">
      <a href="#" class="service-item service-cyber">Cyber Security</a>
      <a href="#" class="service-item service-background">General Background Investigations</a>
      <a href="#" class="service-item service-data">Data Protection</a>
      <a href="#" class="service-item service-physical">Physical Security Services</a>
    </nav>

    <p class="intro">
      <span class="intro-line">Mauris ut leo ut ante laoreet molestie et nec tellus. In blandit mattis urna, at rhoncus sem</span>
      <span class="intro-line">tincidunt quis. Sed velit mauris, pharetra vitae volutpat ac, molestie quis metus. Vestibu-</span>
      <span class="intro-line">lum non risus eu nulla sagittis interdum. Duis ac massa massa.</span>
    </p>

    <div class="cards">
      <article class="card card-cyber">
        <div class="card-media" role="img" aria-label="Photo of blue computer code under a magnifying glass"></div>
        <h2 class="card-title">cyber security</h2>
        <p class="card-text"><span>Voor speelkaartenfabrikant Kaartwerk bouwde Webstudio, in</span><span>samenwerking met communicatiebureau Libel.</span></p>
      </article>
      <article class="card card-physical">
        <div class="card-media" role="img" aria-label="Photo of a security officer in a suit talking on a phone outside a building"></div>
        <h2 class="card-title">physical security</h2>
        <p class="card-text"><span>Voor speelkaartenfabrikant Kaartwerk bouwde Webstudio, in</span><span>samenwerking met communicatiebureau Libel.</span></p>
      </article>
      <article class="card card-data">
        <div class="card-media" role="img" aria-label="Photo of a hooded intruder using a laptop with a flashlight in the dark"></div>
        <h2 class="card-title">data protection</h2>
        <p class="card-text"><span>Voor speelkaartenfabrikant Kaartwerk bouwde Webstudio, in</span><span>samenwerking met communicatiebureau Libel.</span></p>
      </article>
    </div>
  </div>

  <footer class="site-footer">© 2012 QBT Associates. All rights reserved. Terms of Service | Privacy Policy</footer>
</body>
</html>
```